Anzeigengestaltung für Fliesenlegermeister
Zielgruppe
Ich bin ein Fliesenlegermeister und möchte mich selbstständig machen, ich saniere Bäder, Böden mit Fliesen, Fliesenspiegel und ich möchte eine Anzeige in den regionalen Zeitungen machen. Ich spreche alle Altersklassen mit Bädern für Sanierungen, Bodenfliesen und Neubauten an. Reparatur und Silikonarbeiten sowie Trockenbauarbeiten am eigenen Heim .
Aufgabenstellung
Ich möchte gern meine Kontaktdaten und die Farben vom Logo wieder finden,
als Beispiel habe ich meine aktuelle Visitenkarte beigefügt Dort finden sich die Kontaktdaten. Meine Arbeiten sind insbesondere :
Fliesenverlegung
Badsanierung
barrierefreie Bäder
Reparaturarbeiten
Silikonarbeiten
Trockenbau
Ob nun genau alle 6 Punkte in der Anzeige angezeigt werden soll bin ich mir nicht sicher oder ob nur 4 Beschreibungen reichen, damit es nicht zu viel wird.

```html
<!DOCTYPE html>
<html lang="de">
<head>
<meta charset="utf-8">
<title>Anzeige Fliesenlegermeister Jonas Berkel</title>
<link rel="stylesheet" href="https://fonts.googleapis.com/css2?family=Roboto:wght@400;500;700&family=Saira:wght@500;700&display=swap">
<style>
  :root {
    --frame: #4a4a4c;
    --ink: #3d3d3f;
    --line: #d4d4d5;
    --brand-blue: #0d4f9e;
    --bar: #4a4a4c;
    --paper: #ffffff;
    --tile-light: #e3b48f;
    --tile-dark: #c98e6c;
  }
  html, body {
    margin: 0;
    width: 1200px;
    height: 1200px;
    overflow: hidden;
    background: var(--paper);
  }
  .canvas { position: relative; width: 1200px; height: 1200px; }
  .ad {
    position: absolute;
    left: 293px;
    top: 259px;
    width: 892px;
    height: 990px;
    transform: scale(0.6936);
    transform-origin: 0 0;
    box-sizing: border-box;
    border: 6px solid var(--frame);
    background: var(--paper);
    font-family: "Roboto", Arial, sans-serif;
    color: var(--ink);
  }
  .ad__graphics { position: absolute; left: -6px; top: -6px; width: 892px; height: 990px; }
  .headline {
    position: absolute;
    left: 152px; top: 284px;
    width: 575px; height: 120px;
    margin: 0;
    display: flex; flex-direction: column; justify-content: center; align-items: center;
    font-family: "Saira", Arial, sans-serif;
    font-weight: 500;
    font-size: 37px;
    line-height: 44px;
    letter-spacing: 0.5px;
    color: var(--ink);
  }
  .services {
    position: absolute;
    left: 14px; top: 457px;
    margin: 0; padding: 0;
    list-style: none;
  }
  .services li {
    position: relative;
    padding-left: 54px;
    font-weight: 500;
    font-size: 41px;
    line-height: 50.4px;
    white-space: nowrap;
  }
  .services li::before {
    content: "";
    position: absolute;
    left: 12px; top: 16px;
    width: 18px; height: 18px;
    background: var(--brand-blue);
    transform: rotate(45deg);
  }
  .contact-bar {
    position: absolute;
    left: 433px;
    width: 447px;
    height: 83px;
    background: var(--bar);
    color: var(--paper);
    display: flex; align-items: center; justify-content: space-between;
    padding: 0 18px 0 8px;
    box-sizing: border-box;
    font-weight: 700;
    font-size: 47px;
  }
  .contact-bar--phone { top: 466px; }
  .contact-bar--mobile { top: 559px; }
  .contact-bar svg { width: 50px; height: 50px; flex: none; }
  .address {
    position: absolute;
    left: 440px; top: 665px;
    display: flex; gap: 26px;
    font-size: 26px; line-height: 33px;
    font-style: normal;
  }
  .address svg { width: 40px; height: 56px; flex: none; margin-top: 2px; }
  .email {
    position: absolute;
    left: 445px; top: 745px;
    font-size: 26px;
  }
  .brand {
    position: absolute;
    left: 415px; top: 834px;
    height: 93px;
    display: flex; align-items: center;
    padding-left: 20px;
    border-left: 4px solid var(--ink);
    font-family: "Saira", Arial, sans-serif;
    font-weight: 700;
    font-size: 56px;
    color: var(--brand-blue);
    letter-spacing: 1px;
    white-space: nowrap;
  }
</style>
</head>
<body>
<div class="canvas">
  <section class="ad">
    <svg class="ad__graphics" viewBox="0 0 892 990" aria-hidden="false">
      <defs>
        <linearGradient id="tileTone" x1="0" y1="0" x2="1" y2="1">
          <stop offset="0" stop-color="var(--tile-dark)"/>
          <stop offset="0.5" stop-color="var(--tile-light)"/>
          <stop offset="1" stop-color="var(--tile-dark)"/>
        </linearGradient>
      </defs>
      <g fill="none" stroke="var(--line)" stroke-width="12" stroke-linejoin="miter">
        <path d="M350 206 L446 246 L446 292"/>
        <rect x="164" y="296" width="564" height="108" rx="22"/>
        <path d="M446 404 L446 472"/>
        <path d="M446 648 L243 857 L6 857"/>
      </g>
      <polygon role="img" aria-label="Foto: Hände markieren mit Bleistift und Winkel eine Fliese auf einem Fliesenboden"
        points="6,6 886,6 886,210 600,210 450,248 350,210 6,210" fill="url(#tileTone)"/>
    </svg>

    <h1 class="headline"><span>PROFESSIONELLER</span><span>FLIESENLEGERMEISTER</span></h1>

    <ul class="services">
      <li>Fliesenverlegung</li>
      <li>Badsanierung</li>
      <li>barrierefreie Bäder</li>
      <li>Reparaturarbeiten</li>
      <li>Silikonarbeiten</li>
      <li>Trockenbau</li>
    </ul>

    <div class="contact-bar contact-bar--phone">
      <svg viewBox="0 0 50 50" fill="none" stroke="#fff" stroke-width="2.2" stroke-linecap="round" stroke-linejoin="round">
        <path d="M12 10 l6 -2 l5 10 l-4 4 c2 5 5 8 10 10 l4 -4 l10 5 l-2 6 c-1 3 -4 4 -7 3 c-12 -4 -21 -13 -25 -25 c-1 -3 0 -6 3 -7z"/>
        <path d="M28 14 c4 1 7 4 8 8"/><path d="M29 8 c7 1 12 6 13 13"/><path d="M30 2 c9 2 15 8 17 17"/>
      </svg>
      <span>05307/4918265</span>
    </div>
    <div class="contact-bar contact-bar--mobile">
      <svg viewBox="0 0 50 50" fill="none" stroke="#fff" stroke-width="2.2" stroke-linecap="round">
        <rect x="12" y="3" width="26" height="44" rx="4"/>
        <line x1="14" y1="38" x2="36" y2="38"/><line x1="14" y1="9" x2="36" y2="9"/>
        <circle cx="25" cy="42.5" r="1.6"/>
      </svg>
      <span>01598472631</span>
    </div>

    <address class="address">
      <svg viewBox="0 0 40 56" fill="none" stroke="var(--ink)" stroke-width="2.4">
        <path d="M20 44 C12 32 5 24 5 17 A15 15 0 0 1 35 17 C35 24 28 32 20 44z"/>
        <circle cx="20" cy="17" r="6"/>
        <ellipse cx="20" cy="50" rx="8" ry="3"/>
      </svg>
      <span>Ahornweg 24, 38110<br>Braunschweig</span>
    </address>
    <div class="email">info@fliesen-berkel.de</div>

    <div class="brand">JONAS BERKEL</div>
  </section>
</div>
</body>
</html>
```